Creative 1 page website design with html coding needed to go with Game Pre-Registration App

Early Bird Lounge
~Discover games before release~

Website keywords: Simple, slick, stylish
Colors: Black, white, pink (like our logo)

***draft can be created in PSD or HTML***

We have a brand new service called Early Bird Lounge which will be a game app pre-registration service. We already have the icon & UI for the app and we are looking for a slick & stylish corporate website to go with the service.

This will be a corporate website aim for businesses to contact us. Consumers will not be able to pre-register for games here. We do however want consumers to download our app from Nimbus Arcade after landing here.

Some framework we have in mind for 1 page website:
Home - default page showing the UI of the app and Nimbus Arcade icon with store link.
Our Service - quick explanation about our service & it's strength
Clients - logos of our clients
Press-
Pricing - basic usage is free. There will be premium services customers can use on a performance basis (CPA).
Contact Us

Call to action will be 1. Download the app 2. Contact us

We would like to be able to edit the press and clients section with web developer's support.

website in image:
https://www.velquorin.com/

Target Market(s)

Marketing managers of game developer. We want game developers to find out about our service and get in touch with us. The service will only be available in USA.

Midcore gamers in USA: Our end users will be game enthusiasts from US. Male aged 15-35.

Industry/Entity Type

Games

Font styles to use
Sans Serif

Colors
000000
ffffff
e567a6
e34097

Requirements
Must have
• - Only use our colors from the logo attached.
- UI of our app with an Zephyx phone
- Link to Nimbus Arcade Store
- slick & modern design
- Font used: Century Gothic

```html
<!DOCTYPE html>
<html lang="en">
<head>
<meta charset="utf-8">
<title>Early Bird Lounge</title>
<link href="https://fonts.googleapis.com/css2?family=Roboto+Condensed:wght@400;700&family=Roboto:wght@400;500;700&display=swap" rel="stylesheet">
<style>
:root{
  --pink:#e34097;
  --pink-soft:#e567a6;
  --black:#000000;
  --white:#ffffff;
  --ink:#222222;
  --text:#666666;
  --muted:#999999;
  --line:#dddddd;
  --band:#2b2b2b;
  --footer:#0d0d0d;
  --head:"Roboto Condensed",Arial,sans-serif;
  --body:"Roboto",Arial,sans-serif;
}
*{margin:0;padding:0;box-sizing:border-box}
html,body{width:1200px;height:3760px;overflow:hidden}
body{position:relative;background:var(--white);font-family:var(--body);color:var(--text);font-size:13px;line-height:1.5}
.abs{position:absolute}
.topbar{left:0;top:0;width:1200px;height:32px;background:var(--black);display:flex;justify-content:flex-end;align-items:center;gap:16px;padding-right:172px}
.topbar span{color:var(--white);font-size:11px}
.header{left:0;top:32px;width:1200px;height:156px;background:var(--white)}
.brand{display:flex;align-items:center;gap:12px}
.brand-mark{width:62px;height:62px;border-radius:10px;background:var(--pink)}
.brand-name{font-family:var(--head);font-weight:700;font-size:30px;color:var(--pink);line-height:1}
.header .brand{position:absolute;left:172px;top:44px}
.nav{position:absolute;right:172px;top:87px;display:flex;gap:0}
.nav a{display:block;font-family:var(--body);font-size:14px;color:var(--ink);text-decoration:none;padding:12px 17px;height:44px}
.nav a.active{background:var(--pink);color:var(--white)}
.hero{left:0;top:188px;width:1200px;height:432px;background:linear-gradient(135deg,#e14e9d,#d83d8c)}
.hero h1{position:absolute;left:172px;top:88px;width:420px;font-family:var(--head);font-weight:700;font-size:30px;line-height:1.15;color:var(--white);text-transform:uppercase}
.hero p{position:absolute;left:172px;top:176px;width:400px;color:#fbe3f0;font-size:12px;line-height:1.45}
.hero .cta{position:absolute;left:172px;top:262px;background:#2a2a2a;color:var(--white);font-family:var(--head);font-weight:700;font-size:13px;padding:13px 22px}
.hero-art{position:absolute;left:580px;top:10px;width:500px;height:420px;border-radius:14px;background:radial-gradient(circle at 60% 50%,#f3a6cc,#e45ba3 70%)}
.slide-arrow{position:absolute;top:195px;width:34px;height:40px;background:rgba(255,255,255,.35);display:flex;align-items:center;justify-content:center}
.section-title{position:absolute;left:0;width:1200px;text-align:center;font-family:var(--head);font-weight:700;font-size:28px;color:var(--ink);text-transform:uppercase}
.divider{position:absolute;left:172px;width:856px;height:20px}
.divider:before{content:"";position:absolute;left:0;right:0;top:10px;border-top:1px solid var(--line)}
.divider i{position:absolute;left:410px;top:2px;width:36px;height:16px;background:var(--white);border:2px solid #aaa;border-radius:8px}
h2.block{font-family:var(--head);font-weight:700;font-size:26px;color:var(--ink);text-transform:uppercase}
h3.block{font-family:var(--head);font-weight:700;font-size:22px;color:var(--ink)}
.btn{display:inline-block;background:var(--pink);color:var(--white);font-size:12px;padding:5px 12px;border-radius:3px}
.welcome{left:172px;top:668px;width:564px}
.welcome p{margin-top:14px;font-size:12px;line-height:1.55}
.welcome .btn{margin-top:16px;background:#a3195f}
.quote{left:790px;top:668px;width:235px}
.quote .field{height:32px;border:1px solid var(--line);margin-top:8px;font-size:11px;padding:7px 10px;color:var(--muted)}
.quote h2{margin-bottom:14px}
.quote .btn{float:right;margin-top:10px;background:#a3195f}
.services{left:172px;top:1104px;width:856px;display:grid;grid-template-columns:repeat(4,1fr);column-gap:24px;row-gap:40px}
.service{text-align:center}
.service .icon{width:48px;height:48px;margin:0 auto;border-radius:8px;background:var(--pink);display:flex;align-items:center;justify-content:center}
.service h4{margin-top:14px;font-family:var(--head);font-weight:700;font-size:14px;color:var(--ink);text-transform:uppercase;line-height:1.2;height:36px}
.service p{margin-top:6px;font-size:11px;line-height:1.5}
.service a{display:block;margin-top:8px;font-size:11px;color:var(--pink);text-decoration:none}
.app-band{left:0;top:1654px;width:1200px;height:158px;background:var(--band)}
.app-band .brand{position:absolute;left:172px;top:46px}
.app-band .brand-name{color:var(--white)}
.app-band h3{position:absolute;left:530px;top:36px;font-family:var(--head);font-weight:700;font-size:26px;line-height:1.12;color:var(--white);text-transform:uppercase}
.app-band .dl{position:absolute;left:800px;top:46px;width:225px;height:54px;border-radius:5px;background:var(--pink);color:var(--white);font-family:var(--head);font-weight:700;font-size:22px;display:flex;align-items:center;justify-content:center;gap:10px}
.testis{left:172px;top:1996px;width:564px}
.testi{display:flex;gap:14px;margin-top:32px;height:122px}
.photo{width:106px;height:118px;flex:none;background:linear-gradient(160deg,#c8bfb8,#8e8580)}
.testi h5{font-size:12px;color:var(--ink);font-weight:500}
.testi p{font-size:11px;line-height:1.5;margin-top:4px}
.testi .meta{font-size:11px;color:var(--pink);margin-top:4px}
.testis .btn,.news .btn{margin-top:28px;background:#a3195f}
.news{left:790px;top:1996px;width:235px}
.news .item{margin-top:20px}
.news .date{display:inline-block;background:var(--pink);color:var(--white);font-size:11px;padding:2px 8px}
.news p{font-size:11px;line-height:1.5;margin-top:6px}
.news .more{font-size:11px;color:var(--ink);font-weight:500}
.logos{left:172px;top:2516px;width:856px;height:96px;display:flex;align-items:center;justify-content:space-between}
.logos .arrow{width:32px;height:40px;background:var(--pink);display:flex;align-items:center;justify-content:center}
.logos .client{width:132px;height:94px;border:1px solid var(--pink-soft);display:flex;align-items:center;justify-content:center;font-family:var(--body);font-weight:700;font-size:15px;color:var(--ink)}
.contact-band{left:0;top:2782px;width:1200px;height:602px;background:linear-gradient(180deg,#ececec,#dcdcdc)}
.map{position:absolute;left:172px;top:53px;width:355px;height:345px;background:linear-gradient(135deg,#dfe6d7,#cbd8e2)}
.form{position:absolute;left:572px;top:53px;width:453px}
.form .field{background:var(--white);height:44px;margin-bottom:14px;padding:12px 16px;font-size:12px;color:var(--muted)}
.form .field.tall{height:168px}
.form .submit{float:right;background:var(--pink);color:var(--white);width:118px;height:46px;display:flex;align-items:center;justify-content:center;font-family:var(--head);font-size:16px}
.contact-row{position:absolute;left:172px;top:500px;width:856px;display:flex;justify-content:space-between;font-size:11px;color:var(--ink)}
.contact-row div{display:flex;gap:6px;align-items:flex-start}
.footer{left:0;top:3384px;width:1200px;height:314px;background:var(--footer);color:#bbb}
.footer .brand{position:absolute;left:172px;top:110px;flex-direction:column;gap:10px}
.footer .brand-name{color:var(--white);font-size:28px}
.fcol{position:absolute;top:42px;width:190px}
.fcol h6{font-family:var(--head);font-weight:700;font-size:16px;color:var(--white);margin-bottom:12px}
.fcol li{list-style:none;font-size:11px;line-height:1.4;padding:6px 0;border-bottom:1px solid #2a2a2a}
.socials{display:flex;gap:12px;margin-top:14px;font-size:10px;color:var(--white)}
.thumbs{display:grid;grid-template-columns:repeat(3,56px);gap:6px}
.thumbs span{height:56px;background:linear-gradient(135deg,#4a4a6a,#2a2f45)}
.bottombar{left:0;top:3698px;width:1200px;height:62px;background:#1c1c1c;display:flex;align-items:center;justify-content:space-between;padding:0 172px;font-size:11px;color:#999}
.bottombar .tools{display:flex;gap:8px}
.bottombar .tools span{width:32px;height:32px;background:#333;display:flex;align-items:center;justify-content:center}
</style>
</head>
<body>

<div class="abs topbar"><span>Flockr</span><span>Chirpo</span><span>Netlink</span><span>Circlo</span></div>

<header class="abs header">
  <div class="brand"><span class="brand-mark"></span><span class="brand-name">Early Bird Lounge</span></div>
  <nav class="nav">
    <a class="active">Home</a><a>Our Services</a><a>Clients</a><a>Press</a><a>Contact Us</a>
  </nav>
</header>

<section class="abs hero">
  <div class="slide-arrow" style="left:20px"><svg width="12" height="16" viewBox="0 0 12 16"><path d="M9 2 3 8l6 6" fill="none" stroke="#fff" stroke-width="2.5"/></svg></div>
  <h1>Stylish sanctuary for geeky gamers / nerds</h1>
  <p>Donec at justo ut eros ornare vehicula ac et nisl. Nullam urna enim, sagittis quis eros et, blandit viverra orci. Interdum et malesuada fames ac ante ipsum primis in faucibus.</p>
  <div class="cta">CLICK HERE TO VIEW MORE DETAIL ›</div>
  <div class="hero-art" role="img" aria-label="Game character icons around a Zephyx phone showing the Early Bird Lounge app interface"></div>
  <div class="slide-arrow" style="right:20px"><svg width="12" height="16" viewBox="0 0 12 16"><path d="m3 2 6 6-6 6" fill="none" stroke="#fff" stroke-width="2.5"/></svg></div>
</section>

<section class="abs welcome">
  <h2 class="block">Welcome to Early Bird Lounge</h2>
  <p>Donec at justo ut eros ornare vehicula ac et nisl. Nullam urna enim, sagittis quis eros et, blandit viverra orci. Interdum et malesuada fames ac ante ipsum primis in faucibus. Duis nec pellentesque urna, quis consectetur nibh. Fusce facilisis lorem sed leo porttitor mollis. Aliquam consectetur libero id erat tincidunt, sit amet mollis dolor ornare. Ut orci augue, luctus ac porta ut, posuere sed felis.</p>
  <p>Sed posuere magna vitae sodales imperdiet. Sed pulvinar velit eu eros imperdiet, in blandit ante hendrerit. Donec neque dui, blandit nec vulputate vel, consectetur at urna. Pellentesque habitant morbi tristique senectus et netus et malesuada fames ac turpis egestas. Proin porta ligula quam.</p>
  <span class="btn">View more ›</span>
</section>

<section class="abs quote">
  <h2 class="block">Get a Quote</h2>
  <div class="field">Name</div><div class="field">Phone</div><div class="field">Email</div><div class="field">Zip</div>
  <span class="btn">Submit ›</span>
</section>

<div class="divider" style="top:994px"><i></i></div>
<h2 class="section-title" style="top:1036px">Our Services</h2>

<section class="abs services">
  <div class="service"><div class="icon"><svg width="22" height="22"><circle cx="11" cy="11" r="8" fill="#fff"/></svg></div><h4>Praesent placerat ex sed</h4><p>Donec at justo ut eros ornare vehicula ac et nisl. Nullam urna enim, sagittis quis eros et, blandit viverra orci. Interdum et mal.</p><a>View more ›</a></div>
  <div class="service"><div class="icon"><svg width="22" height="22"><path d="M4 18 18 4" stroke="#fff" stroke-width="4"/></svg></div><h4>Sed posuere magna vitae</h4><p>Donec at justo ut eros ornare vehicula ac et nisl. Nullam urna enim, sagittis quis eros et, blandit viverra orci. Interdum et mal.</p><a>View more ›</a></div>
  <div class="service"><div class="icon"><svg width="22" height="22"><rect x="3" y="10" width="4" height="9" fill="#fff"/><rect x="9" y="6" width="4" height="13" fill="#fff"/><rect x="15" y="3" width="4" height="16" fill="#fff"/></svg></div><h4>Donec neque dui, blandit nec</h4><p>Donec at justo ut eros ornare vehicula ac et nisl. Nullam urna enim, sagittis quis eros et, blandit viverra orci. Interdum et mal.</p><a>View more ›</a></div>
  <div class="service"><div class="icon"><svg width="22" height="22"><circle cx="8" cy="8" r="5" fill="#fff"/><circle cx="15" cy="15" r="5" fill="#fff"/></svg></div><h4>Nullam urna enim, sagittis quis</h4><p>Donec at justo ut eros ornare vehicula ac et nisl. Nullam urna enim, sagittis quis eros et, blandit viverra orci. Interdum et mal.</p><a>View more ›</a></div>
  <div class="service"><div class="icon"><svg width="22" height="22"><circle cx="11" cy="11" r="8" fill="none" stroke="#fff" stroke-width="3"/><path d="M11 7v8M7 11h8" stroke="#fff" stroke-width="2"/></svg></div><h4>Praesent placerat ex sed</h4><p>Donec at justo ut eros ornare vehicula ac et nisl. Nullam urna enim, sagittis quis eros et, blandit viverra orci. Interdum et mal.</p><a>View more ›</a></div>
  <div class="service"><div class="icon"><svg width="22" height="22"><path d="M5 17 17 5M5 17l-2 3 3-2" stroke="#fff" stroke-width="3" fill="none"/></svg></div><h4>Sed posuere magna vitae</h4><p>Donec at justo ut eros ornare vehicula ac et nisl. Nullam urna enim, sagittis quis eros et, blandit viverra orci. Interdum et mal.</p><a>View more ›</a></div>
  <div class="service"><div class="icon"><svg width="22" height="22"><path d="M3 19 19 3l-4 16-4-6z" fill="#fff"/></svg></div><h4>Donec neque dui, blandit nec</h4><p>Donec at justo ut eros ornare vehicula ac et nisl. Nullam urna enim, sagittis quis eros et, blandit viverra orci. Interdum et mal.</p><a>View more ›</a></div>
  <div class="service"><div class="icon"><svg width="22" height="22"><rect x="4" y="3" width="14" height="16" fill="none" stroke="#fff" stroke-width="2.5"/><path d="M7 8h8M7 12h8M7 16h5" stroke="#fff" stroke-width="2"/></svg></div><h4>Nullam urna enim, sagittis quis</h4><p>Donec at justo ut eros ornare vehicula ac et nisl. Nullam urna enim, sagittis quis eros et, blandit viverra orci. Interdum et mal.</p><a>View more ›</a></div>
</section>

<section class="abs app-band">
  <div class="brand"><span class="brand-mark"></span><span class="brand-name">Early Bird Lounge</span></div>
  <h3>Game App<br>Pre-Registration<br>Service</h3>
  <div class="dl">DOWNLOAD HERE <svg width="20" height="20" viewBox="0 0 20 20"><circle cx="10" cy="10" r="9" fill="#fff"/><path d="m8 5 5 5-5 5" fill="none" stroke="#e34097" stroke-width="2.5"/></svg></div>
</section>

<div class="divider" style="top:1864px"><i></i></div>
<h2 class="section-title" style="top:1902px">Clients</h2>

<section class="abs testis">
  <h3 class="block">Client Testimonials</h3>
  <div class="testi" style="margin-top:46px">
    <div class="photo" role="img" aria-label="Portrait photo of a client"></div>
    <div><h5>Dalen Pryce – Orbwell</h5><p>Li Europan lingues es membres del sam familie. Lor separat existentie es un myth. Por scientie, musica, sport etc. litot Europa usa li sam. Donec at justo ut eros ornare vehicula ac et nisl. Nullam urna enim, sagittis quis eros et, blandit viverra orci. Interdum et malesuada fames ac ante ipsum primis in faucibus vocabular.</p><p class="meta">28 June 2014 · Tomas Vell</p></div>
  </div>
  <div class="testi">
    <div class="photo" role="img" aria-label="Portrait photo of a client"></div>
    <div><h5>Dalen Pryce – Orbwell</h5><p>Li Europan lingues es membres del sam familie. Lor separat existentie es un myth. Por scientie, musica, sport etc. litot Europa usa li sam. Donec at justo ut eros ornare vehicula ac et nisl. Nullam urna enim, sagittis quis eros et, blandit viverra orci. Interdum et malesuada fames ac ante ipsum primis in faucibus vocabular.</p><p class="meta">28 June 2014 · Tomas Vell</p></div>
  </div>
  <span class="btn">View All ›</span>
</section>

<section class="abs news">
  <h3 class="block">Latest News</h3>
  <div class="item"><span class="date">21 Sep</span><p>Donec metus lacus, sagittis id ligula a, porttitor hen drerit nunc. Mauris varius enim.</p><span class="more">Read more ›</span></div>
  <div class="item"><span class="date">20 Sep</span><p>Donec metus lacus, sagittis id ligula a, porttitor hen drerit nunc. Mauris varius enim.</p><span class="more">Read more ›</span></div>
  <div class="item"><span class="date">19 Sep</span><p>Donec metus lacus, sagittis id ligula a, porttitor hen drerit nunc. Mauris varius enim.</p><span class="more">Read more ›</span></div>
  <span class="btn">View All ›</span>
</section>

<section class="abs logos">
  <span class="arrow"><svg width="12" height="16" viewBox="0 0 12 16"><path d="M9 2 3 8l6 6" fill="none" stroke="#fff" stroke-width="2.5"/></svg></span>
  <span class="client">Kestrova</span>
  <span class="client">Brindlemoor</span>
  <span class="client">Talvex</span>
  <span class="client">Orchard Hollow</span>
  <span class="client">Quillspace</span>
  <span class="arrow"><svg width="12" height="16" viewBox="0 0 12 16"><path d="m3 2 6 6-6 6" fill="none" stroke="#fff" stroke-width="2.5"/></svg></span>
</section>

<div class="divider" style="top:2664px"><i></i></div>
<h2 class="section-title" style="top:2704px">Contact Us</h2>

<section class="abs contact-band" role="img" aria-label="Faded city photo backdrop behind the contact area">
  <div class="map" role="img" aria-label="Street map with office location marker"></div>
  <div class="form">
    <div class="field">Your Name</div>
    <div class="field">Your Email</div>
    <div class="field tall">Your Message</div>
    <div class="submit">SUBMIT</div>
  </div>
  <div class="contact-row">
    <div><svg width="12" height="14" viewBox="0 0 12 14"><path d="M6 0a5 5 0 0 1 5 5c0 4-5 9-5 9S1 9 1 5a5 5 0 0 1 5-5z" fill="#e34097"/></svg><span>14 Harlow Crest Lane<br>Faucibus quis magna sollicitudin</span></div>
    <div><svg width="12" height="12" viewBox="0 0 12 12"><path d="M2 1h3l1 3-2 1a7 7 0 0 0 3 3l1-2 3 1v3c-6 0-10-4-10-9z" fill="#e34097"/></svg><span>29 40 61 52</span></div>
    <div><svg width="14" height="10" viewBox="0 0 14 10"><rect width="14" height="10" fill="#e34097"/><path d="m1 1 6 5 6-5" fill="none" stroke="#fff"/></svg><span>info@earlybirdlounge.com</span></div>
    <div><svg width="12" height="12" viewBox="0 0 12 12"><path d="M2 1h3l1 3-2 1a7 7 0 0 0 3 3l1-2 3 1v3c-6 0-10-4-10-9z" fill="#e34097"/></svg><span>29 40 61 52</span></div>
    <div><svg width="12" height="12" viewBox="0 0 12 12"><circle cx="6" cy="6" r="5" fill="none" stroke="#e34097" stroke-width="2"/></svg><span>http://earlybirdlounge.com</span></div>
  </div>
</section>

<footer class="abs footer">
  <div class="brand"><span class="brand-mark"></span><span class="brand-name">Early Bird Lounge</span></div>
  <div class="fcol" style="left:400px">
    <h6>Latest Post</h6>
    <ul><li>Curabitur ac neque et arcu</li><li>Proin vel mauris diam</li><li>Proin urna enim semper</li><li>Nunc adipiscing semper nisl</li><li>Pellentesque tempus amet</li></ul>
  </div>
  <div class="fcol" style="left:620px">
    <h6>Quick Links</h6>
    <ul><li>Curabitur ac neque et arcu</li><li>Proin vel mauris diam</li><li>Proin urna enim semper</li><li>Nunc adipiscing semper nisl</li></ul>
    <div class="socials"><span>Flockr</span><span>Chirpo</span><span>Netlink</span><span>Circlo</span></div>
  </div>
  <div class="fcol" style="left:840px">
    <h6>Photostream</h6>
    <div class="thumbs" role="img" aria-label="Grid of six game artwork thumbnails"><span></span><span></span><span></span><span></span><span></span><span></span></div>
  </div>
</footer>

<div class="abs bottombar">
  <span>Copyright © 2014 · All rights reserved</span>
  <div class="tools">
    <span><svg width="12" height="12" viewBox="0 0 12 12"><rect x="1" y="1" width="10" height="10" fill="none" stroke="#ccc" stroke-width="1.5"/></svg></span>
    <span><svg width="12" height="10" viewBox="0 0 12 10"><path d="M1 8 6 3l5 5" fill="none" stroke="#ccc" stroke-width="2"/></svg></span>
  </div>
</div>

</body>
</html>
```